Engineering Consultant Business Card

I'm starting a new business as a high-end engineering consultant in a niche field. I've attached the jpg for my logo plus the branding guideline document that I've been following. You can see my business website here: www.tarvikworks.com
I'd like a business card that has the logo on one side, then the other side has (in any order): Tarvik Works, Inc.
Dana Whitlock
President and Chief EMC Engineer
www.tarvikworks.com
dana@tarvikworks.com
Optional: motto "We will solve your EMC problems as early as possible—ideally before they even start."
I'm not planning on including a phone number
Target Market(s)
Businesses, especially makers of electronics hardware
Industry/Entity Type
Electrical engineering
Contact Information for Business Card
Company name, my name, website, email

```html
<!DOCTYPE html>
<html lang="en">
<head>
<meta charset="utf-8">
<title>Tarvik Works, Inc. — Business Card</title>
<link rel="stylesheet" href="https://fonts.googleapis.com/css2?family=Roboto:wght@300;400;500&display=swap">
<style>
  :root {
    --backdrop: #e4e4e4;
    --card-white: #ffffff;
    --teal: #7cc5d4;
    --teal-tint: #e9f5f8;
    --teal-mark: #a3d6e2;
    --brand-blue: #2b3f96;
    --text-light: #ffffff;
  }
  * { box-sizing: border-box; margin: 0; padding: 0; }
  html, body {
    width: 1200px; height: 1200px; overflow: hidden;
    background: var(--backdrop);
    font-family: "Roboto", sans-serif;
  }
  .card {
    position: absolute;
    left: 165px;
    width: 872px;
    height: 508px;
    overflow: hidden;
  }
  .card-front { top: 71px; background: var(--card-white); }
  .card-back { top: 621px; height: 510px; background: var(--teal); }

  .front-shapes { position: absolute; inset: 0; width: 100%; height: 100%; }

  .brand-lockup {
    position: absolute;
    left: 72px; top: 84px;
    width: 300px;
    text-align: center;
    color: var(--brand-blue);
  }
  .brand-mark {
    display: flex; align-items: center; justify-content: center; gap: 14px;
    height: 116px;
  }
  .brand-dot {
    width: 44px; height: 44px; border-radius: 50%;
    background: var(--brand-blue);
  }
  .brand-word {
    font-size: 46px; font-weight: 500; letter-spacing: 1px;
    color: var(--brand-blue);
  }
  .company-name {
    margin-top: 14px;
    font-size: 33px; font-weight: 500;
    color: var(--brand-blue);
  }

  .person {
    position: absolute;
    right: 50px; top: 258px;
    text-align: right;
    color: var(--text-light);
  }
  .person-name {
    font-size: 36px; font-weight: 400; letter-spacing: 0.5px; line-height: 1.1;
  }
  .person-title {
    margin-top: 8px;
    font-size: 20px; font-weight: 300;
  }

  .contact {
    position: absolute;
    right: 46px; top: 376px;
    list-style: none;
    color: var(--text-light);
    font-size: 24px; font-weight: 300;
  }
  .contact-item {
    display: flex; align-items: center; justify-content: flex-end; gap: 14px;
    height: 33px;
  }
  .contact-icon { width: 16px; height: 16px; fill: var(--text-light); }

  .back-mark {
    position: absolute; inset: 0;
    display: flex; align-items: center; justify-content: center;
    font-size: 84px; font-weight: 500; letter-spacing: 2px;
    color: var(--teal-mark);
  }
</style>
</head>
<body>

<section class="card card-front" aria-label="Business card front">
  <svg class="front-shapes" viewBox="0 0 872 508" preserveAspectRatio="none" aria-hidden="true">
    <polygon points="405,0 872,0 635,132" fill="var(--teal-tint)"/>
    <polygon points="0,508 872,0 872,508" fill="var(--teal)"/>
  </svg>

  <div class="brand-lockup">
    <div class="brand-mark">
      <span class="brand-dot"></span>
      <span class="brand-word">TARVIK</span>
    </div>
    <p class="company-name">Tarvik Works, Inc.</p>
  </div>

  <div class="person">
    <h1 class="person-name">DANA WHITLOCK</h1>
    <p class="person-title">President and Chief EMC Engineer</p>
  </div>

  <ul class="contact">
    <li class="contact-item">
      <span>www.tarvikworks.com</span>
      <svg class="contact-icon" viewBox="0 0 16 16" aria-hidden="true">
        <path d="M8 1a7 7 0 1 0 0 14A7 7 0 0 0 8 1zm0 1.6c.9 0 1.8 1.6 2.1 4.4H5.9C6.2 4.2 7.1 2.6 8 2.6zM4.4 7H2.7a5.4 5.4 0 0 1 3-4C5 4 4.5 5.4 4.4 7zm0 2c.1 1.6.6 3 1.3 4a5.4 5.4 0 0 1-3-4zm1.5 0h4.2c-.3 2.8-1.2 4.4-2.1 4.4S6.2 11.8 5.9 9zm5.7 0h1.7a5.4 5.4 0 0 1-3 4c.7-1 1.2-2.4 1.3-4zm0-2c-.1-1.6-.6-3-1.3-4a5.4 5.4 0 0 1 3 4z"/>
      </svg>
    </li>
    <li class="contact-item">
      <span>dana@tarvikworks.com</span>
      <svg class="contact-icon" viewBox="0 0 16 16" aria-hidden="true">
        <path d="M8 1a5 5 0 0 0-5 5c0 3.6 5 9 5 9s5-5.4 5-9a5 5 0 0 0-5-5zm0 6.8A1.8 1.8 0 1 1 8 4.2a1.8 1.8 0 0 1 0 3.6z"/>
      </svg>
    </li>
  </ul>
</section>

<section class="card card-back" aria-label="Business card back">
  <div class="back-mark">Tarvik</div>
</section>

</body>
</html>
```